Beautiful, sharp, website design for family-run property development company.

We are property developers in Kent (south east of London) who want to see the local town change. We are the only local property developer that is a family run business, focussing primarily on converting old, dilapidated Victorian buildings into beautiful residential spaces. Unlike other national developers, we work to regenerate buildings to create new employment opportunities, housing, and revive the town Centre .

Target Market(s)

1. Investors and Joint Venture partners - people with money to invest in property
2. Buyers of property - 25 to 40 year old, young professionals.
3. Commercial funders (people lending money to our projects
4. Professional team: Architects, builders, Estate agent who want to work with us

Industry/Entity Type

Real Estate Development

Coding

Number of Pages Required

Font styles to use
• Please follow the brief of stylish, elegant, modern

Colors

Designer to choose colors to be used in the design.

Requirements
Must have
• Please use these websites as a reference of what we are looking to achieve.
• http://brekmorestudio.com/#page5
• https://palvendro.co.uk/
• http://tamberfold.co.uk/
• http://www.thequarvishgroup.co.uk/about-quarvish
• Clean, simple, elegant, minimal design.
• Images of interiors of houses that have been converted from old buildings
• Images of farm buildings e.g. barns that have been converted to new homes or offices. Images of properties that may have been an old factory or old commercial property that is now a trendy apartment.
• Please use images of properties and interiors that are from the South East of England (including Kent, Surrey, Sussex, Hampshire, Dorset). There is a distinct style of housing in this part of England.
Nice to have
• Colours consistent with our brand colour palette (attached)

```html
<!DOCTYPE html>
<html lang="en">
<head>
<meta charset="utf-8">
<title>Larchmere Homes</title>
<link href="https://fonts.googleapis.com/css2?family=Maven+Pro:wght@400;500&family=Roboto:wght@400;500;700&display=swap" rel="stylesheet">
<style>
:root{
  --teal:#7d9b94;
  --teal-dark:#6b8881;
  --stone:#ebe9e6;
  --ink:#1a1a1a;
  --muted:#555;
  --black:#0e0e0e;
  --black-2:#050505;
  --white:#fff;
}
*{margin:0;padding:0;box-sizing:border-box}
html,body{width:1200px;height:5034px;overflow:hidden;background:var(--white)}
body{position:relative;font-family:'Roboto',Arial,sans-serif;color:var(--ink)}
.abs{position:absolute}
.display{font-family:'Maven Pro',Arial,sans-serif;font-weight:400;color:var(--ink)}
.btn{position:absolute;background:var(--teal);color:var(--white);font-size:11px;font-weight:700;letter-spacing:.6px;text-transform:uppercase;display:flex;align-items:center;justify-content:center}
.photo{position:absolute}
.brand{font-family:'Maven Pro',Arial,sans-serif;font-weight:500;color:var(--teal);font-size:19px;letter-spacing:1px;text-transform:uppercase;display:flex;align-items:center;gap:10px}
.brand .mark{width:14px;height:14px;border:2px solid var(--teal)}
.eyebrow{font-size:10px;font-weight:700;letter-spacing:1px;color:var(--teal);text-transform:uppercase;display:flex;align-items:center;gap:10px}
.eyebrow::before,.eyebrow.center::after{content:"";width:34px;height:1px;background:var(--ink)}
.copy{font-size:11.5px;line-height:17px;color:var(--muted)}

/* sidebar */
.menu-btn{left:29px;top:23px;width:44px;height:44px;background:var(--teal);display:flex;flex-direction:column;justify-content:center;align-items:center;gap:5px}
.menu-btn span{width:22px;height:2px;background:var(--white)}
.follow-line{left:42px;top:290px;width:1px;height:70px;background:var(--ink)}
.follow-label{left:24px;top:388px;transform:rotate(-90deg);font-size:10px;font-weight:700;letter-spacing:.5px;white-space:nowrap}
.social-stack{left:25px;top:445px;width:33px}
.social-stack div{width:33px;height:33px;border:1.5px solid var(--ink);margin-top:-1.5px;display:flex;align-items:center;justify-content:center}
.social-stack div::after{content:"";width:7px;height:7px;background:var(--ink);border-radius:50%}

/* hero */
.hero-panel{left:100px;top:0;width:883px;height:540px;background:var(--stone)}
.hero-frame{left:584px;top:88px;width:616px;height:556px;background:var(--white)}
.hero-title{left:160px;top:190px;font-size:40px;line-height:50px}
.hero-rule{left:162px;top:306px;width:58px;height:2px;background:var(--ink)}
.hero-copy{left:162px;top:332px;width:320px}
.call{left:1034px;top:28px;display:flex;gap:10px;align-items:flex-start}
.call .t1{font-size:12px;color:var(--ink)}
.call .t2{font-size:10px;color:var(--teal);margin-top:2px}
.slider-line{left:387px;top:587px;width:66px;height:1.5px;background:var(--ink)}
.slide-num{top:571px;width:33px;height:33px;font-size:10px;font-weight:700;display:flex;align-items:center;justify-content:center}
.slide-num.active{border:1.5px solid var(--ink)}

/* about */
.about-title{left:653px;top:756px;font-size:40px;line-height:49px}
.quote-row{left:653px;top:886px;width:300px;display:flex;gap:12px}
.quote-row p{font-size:11px;font-weight:700;line-height:16px}
.qmark{font-family:'Maven Pro',sans-serif;font-weight:500;font-size:40px;line-height:30px;color:var(--teal)}
.about-copy{left:653px;top:936px;width:380px;font-size:10.5px;line-height:16px}

/* projects */
.section-title{left:0;width:1290px;text-align:center;font-size:40px}
.project-panel{position:absolute;background:var(--stone);width:845px;height:425px}
.project-title{font-size:20px}
.project-copy{width:320px;margin-top:14px;font-size:10.5px;line-height:16px}
.pic-split{position:absolute;width:446px;height:336px;display:flex}
.pic-split .handle{position:absolute;top:50%;width:18px;height:18px;margin:-9px 0 0 -9px;border-radius:50%;background:var(--white)}

/* contact */
.contact-panel{left:174px;top:3099px;width:475px;height:405px;background:rgba(255,255,255,.86)}
.contact-title{left:240px;top:3162px;font-size:17px}
.field{position:absolute;left:240px;width:342px;border-bottom:1px solid #444;font-size:11px;padding-bottom:3px}

/* testimonials */
.testi-band{left:102px;top:3645px;width:1090px;height:615px;background:var(--stone)}
.card{position:absolute;top:3869px;width:305px;height:271px;background:var(--white);text-align:center}
.card .q{font-family:'Maven Pro',sans-serif;font-weight:500;font-size:40px;color:var(--teal);line-height:30px;margin-top:6px}
.card p{font-size:11px;font-weight:700;line-height:19px;padding:12px 22px 0}
.card .name{font-family:'Maven Pro',sans-serif;font-size:17px;margin-top:24px}
.avatar{position:absolute;top:4150px;width:72px;height:72px;background:linear-gradient(160deg,#d8dde2,#8a95a2)}

/* gallery + footer */
.gallery{left:102px;top:4345px;width:1098px;height:209px;display:flex}
.gallery div{flex:1}
.footer{left:102px;top:4554px;width:1098px;height:358px;background:var(--black)}
.footer-base{left:102px;top:4912px;width:1098px;height:122px;background:var(--black-2)}
.news-title{left:172px;top:4652px;font-size:20px;color:var(--white)}
.news-field{left:172px;top:4678px;width:575px;border-bottom:1px solid #666;font-size:10px;color:var(--white);padding-bottom:6px}
.divider{left:860px;top:4632px;width:1px;height:235px;background:#444}
.connect{left:972px;top:4652px;width:124px;text-align:center;font-size:16px;color:var(--white);font-family:'Maven Pro',sans-serif}
.s-dot{position:absolute;width:12px;height:12px;border-radius:50%;background:var(--white)}
.back-top{left:1140px;top:4628px;transform:rotate(-90deg);font-size:10px;font-weight:700;color:var(--white);white-space:nowrap}
.back-line{left:1166px;top:4665px;width:1px;height:55px;background:var(--white)}
.foot-info{left:520px;top:4969px;display:flex;gap:26px;font-size:10.5px;font-weight:700;color:var(--white);align-items:center}
.foot-info span{display:flex;gap:7px;align-items:center}
</style>
</head>
<body>

<!-- sidebar -->
<div class="abs menu-btn"><span></span><span></span><span></span></div>
<div class="abs follow-line"></div>
<div class="abs follow-label">FOLLOW US</div>
<div class="abs social-stack" aria-label="Social links"><div></div><div></div><div></div></div>

<!-- hero -->
<div class="abs hero-panel"></div>
<div class="abs hero-frame"></div>
<div class="abs brand" style="left:162px;top:70px"><span class="mark"></span>Larchmere Homes</div>
<h1 class="abs display hero-title">Find a Home You<br>Love!</h1>
<div class="abs hero-rule"></div>
<p class="abs copy hero-copy">Excepteur sint occaecat cupidatat non proident sunt in culpa qui officia deserunt mollit anim</p>
<div class="btn" style="left:162px;top:400px;width:139px;height:49px">View Now</div>
<div class="abs call">
  <svg width="20" height="20" viewBox="0 0 24 24" fill="none" stroke="#7d9b94" stroke-width="1.6"><path d="M5 3h4l2 5-3 2a11 11 0 0 0 6 6l2-3 5 2v4a2 2 0 0 1-2 2A17 17 0 0 1 3 5a2 2 0 0 1 2-2z"/></svg>
  <div><div class="t1">Call Us Now!</div><div class="t2">0 000 000 0000</div></div>
</div>
<div class="photo" role="img" aria-label="Bright living room with sofas, ottoman and fireplace" style="left:600px;top:105px;width:594px;height:524px;background:linear-gradient(135deg,#f1efea 0%,#dcd7cd 45%,#b9b1a3 75%,#8c8478 100%)"></div>
<div class="abs slider-line"></div>
<div class="abs slide-num active" style="left:471px">01</div>
<div class="abs slide-num" style="left:508px">02</div>
<div class="abs slide-num" style="left:545px">03</div>

<!-- about -->
<div class="photo" role="img" aria-label="Restored white period mansion with lawn" style="left:170px;top:713px;width:381px;height:456px;background:linear-gradient(180deg,#a9c5e0 0%,#e8e6df 35%,#ece9e0 65%,#6f8b4b 85%,#4e6a34 100%)"></div>
<div class="photo" role="img" aria-label="Red brick Victorian house with garden" style="left:336px;top:1049px;width:249px;height:171px;background:var(--white)"></div>
<div class="photo" role="img" aria-label="Red brick Victorian house with garden" style="left:344px;top:1057px;width:233px;height:155px;background:linear-gradient(180deg,#c7d8e8 0%,#9c5a45 45%,#7a4432 65%,#55793a 100%)"></div>
<div class="abs eyebrow" style="left:653px;top:733px">Who We Are</div>
<h2 class="abs display about-title">Rejuvinating<br>Old Properties</h2>
<div class="abs quote-row"><span class="qmark">”</span><p>Quis autem vel eum iure reprehenderit qui in ea voluptate velit esse quam nihil</p></div>
<p class="abs copy about-copy">Nam libero tempore, cum soluta nobis est eligendi optio cumque nihil impedit quo minus id quod maxime placeat facere possimus, omnis voluptas assumenda est, omnis dolor repellendus. officiis debitis aut rerum necessitatibus saepe eveniet</p>
<div class="btn" style="left:653px;top:1052px;width:151px;height:49px">About Us</div>

<!-- projects -->
<div class="abs eyebrow center" style="left:572px;top:1320px">Our Works</div>
<h2 class="abs display section-title" style="top:1345px">Recent Projects</h2>

<div class="project-panel" style="left:172px;top:1470px">
  <div style="padding:158px 0 0 42px"><div class="display project-title">Temporibus autem quibusdam</div>
  <p class="copy project-copy">Itaque earum rerum hic tenetur a sapiente delectus, ut aut reiciendis voluptatibus maiores alias aut perferendis doloribus asperiores repellat</p></div>
</div>
<div class="pic-split" role="img" aria-label="Bedroom with green walls and cream bench, before and after" style="left:676px;top:1470px">
  <div style="width:156px;background:linear-gradient(160deg,#c9b9a0,#7d6d59)"></div>
  <div style="flex:1;background:linear-gradient(160deg,#6b7560 0%,#ece7dc 50%,#b9ab96 100%)"></div>
  <span class="handle" style="left:156px"></span>
</div>

<div class="project-panel" style="left:303px;top:1947px">
  <div style="padding:152px 0 0 409px"><div class="display project-title">Quis autem vel eum iure nostrum</div>
  <p class="copy project-copy">Neque porro quisquam est, qui dolorem ipsum quia dolor sit amet consectetur adipisci velit sed quia non numquam eius modi aliquid ex ea commodi</p></div>
</div>
<div class="photo" style="left:186px;top:1940px;width:473px;height:357px;background:var(--white)"></div>
<div class="pic-split" role="img" aria-label="Renovated kitchen with dark cabinets and skylight, before and after" style="left:197px;top:1947px">
  <div style="width:158px;background:linear-gradient(160deg,#d8d3c3,#7a7566)"></div>
  <div style="flex:1;background:linear-gradient(150deg,#f3f2ef 0%,#d9d6d0 55%,#3e4048 80%,#2c2d32 100%)"></div>
</div>

<div class="project-panel" style="left:172px;top:2422px">
  <div style="padding:150px 0 0 42px"><div class="display project-title">Sunt in culpa qui officia deserunt</div>
  <p class="copy project-copy">Neque porro quisquam est qui dolorem ipsum quia dolor sit amet consectetur adipisci velit sed quia non numquam eius modi tempora incidunt ut labore et dolore</p></div>
</div>
<div class="pic-split" role="img" aria-label="Drawing room with bay window and leather ottoman, before and after" style="left:676px;top:2422px">
  <div style="width:116px;background:linear-gradient(160deg,#d2c4ae,#8a4c3e)"></div>
  <div style="flex:1;background:linear-gradient(160deg,#e9e4d8 0%,#cfc6b3 50%,#6e4a34 100%)"></div>
  <span class="handle" style="left:116px"></span>
</div>

<div class="btn" style="left:559px;top:2889px;width:157px;height:41px">View More</div>

<!-- contact -->
<div class="photo" role="img" aria-label="Brick and tile-hung Kent family house under blue sky" style="left:102px;top:2973px;width:1090px;height:672px;background:linear-gradient(180deg,#5b8fd0 0%,#9cc0e6 30%,#a0664a 55%,#7a4f3a 72%,#9a9892 88%,#7f7d78 100%)"></div>
<div class="abs contact-panel"></div>
<h3 class="abs display contact-title">Contact Us</h3>
<p class="abs copy" style="left:240px;top:3208px;width:350px;font-size:10.5px">Excepteur sint occaecat cupidatat non proident sunt in culpa qui officia deserunt mollit anim id est laborum</p>
<div class="field" style="top:3280px">Name*</div>
<div class="field" style="top:3315px">Email*</div>
<div class="field" style="top:3350px">Message*</div>
<div class="btn" style="left:240px;top:3402px;width:174px;height:39px">Send Us A Message</div>

<!-- testimonials -->
<div class="abs testi-band"></div>
<div class="abs eyebrow center" style="left:562px;top:3733px">Testimonials</div>
<h2 class="abs display section-title" style="top:3760px">People Trust Us</h2>
<div class="card" style="left:162px"><div class="q">”</div><p>Quis autem vel eum iure reprehenderit qui in ea voluptate velit esse quam nihil molestiae consequatur, vel illum qui dolorem eum fugiat quo voluptas nulla pariatur sed quia non numquam eius modi tempora incidunt</p><div class="name">John Doe</div></div>
<div class="card" style="left:489px"><div class="q">”</div><p>Quis autem vel eum iure reprehenderit qui in ea voluptate velit esse quam nihil molestiae consequatur, vel illum qui dolorem eum fugiat quo voluptas nulla pariatur sed quia non numquam eius modi tempora incidunt</p><div class="name">John Doe</div></div>
<div class="card" style="left:817px"><div class="q">”</div><p>Quis autem vel eum iure reprehenderit qui in ea voluptate velit esse quam nihil molestiae consequatur, vel illum qui dolorem eum fugiat quo voluptas nulla pariatur sed quia non numquam eius modi tempora incidunt</p><div class="name">John Doe</div></div>
<div class="avatar" role="img" aria-label="Client portrait" style="left:277px"></div>
<div class="avatar" role="img" aria-label="Client portrait" style="left:603px"></div>
<div class="avatar" role="img" aria-label="Client portrait" style="left:931px"></div>

<!-- gallery -->
<div class="abs gallery" role="img" aria-label="Strip of five converted home interiors">
  <div style="background:linear-gradient(160deg,#e6ddd0,#8f7f6c)"></div>
  <div style="background:linear-gradient(160deg,#c8d6de,#6d7f86)"></div>
  <div style="background:linear-gradient(160deg,#ece8e1,#7a7e8c)"></div>
  <div style="background:linear-gradient(160deg,#e7e4df,#4a4a4e)"></div>
  <div style="background:linear-gradient(160deg,#f1ece4,#a88d6c)"></div>
</div>

<!-- footer -->
<div class="abs footer"></div>
<div class="abs footer-base"></div>
<h3 class="abs display news-title">Subscribe To Our Newsletter</h3>
<div class="abs news-field" style="top:4688px">Email...</div>
<div class="btn" style="left:172px;top:4760px;width:125px;height:35px;font-size:10px">Subscribe</div>
<div class="abs divider"></div>
<div class="abs connect">Connect With Us</div>
<span class="s-dot" style="left:989px;top:4705px"></span>
<span class="s-dot" style="left:1065px;top:4705px"></span>
<span class="s-dot" style="left:989px;top:4767px"></span>
<span class="s-dot" style="left:1065px;top:4767px"></span>
<div class="abs back-top">BACK TO TOP</div>
<div class="abs back-line"></div>
<div class="abs brand" style="left:160px;top:4964px;font-size:17px"><span class="mark"></span>Larchmere Homes</div>
<div class="abs foot-info">
  <span><svg width="12" height="12" viewBox="0 0 24 24" fill="#fff"><path d="M5 2h4l2 6-3 2a12 12 0 0 0 6 6l2-3 6 2v4a3 3 0 0 1-3 3A19 19 0 0 1 2 5a3 3 0 0 1 3-3z"/></svg>0 000 000 0000</span>
  <span><svg width="13" height="10" viewBox="0 0 26 20" fill="#fff"><path d="M0 0h26v20H0z"/><path d="M1 1l12 9 12-9" stroke="#0e0e0e" stroke-width="2" fill="none"/></svg>info@larchmerehomes.com</span>
  <span>©Copyright information here</span>
</div>

</body>
</html>
```